Stationary for Halcyon Elite Las Vegas
Business cards & letter head, etc
Stationary for Halcyon Elite Las Vegas - Hospitality Industry
Creative Brief
Use same font as used in my logo
Just make it look nice & professional
Professional
Miles Grant
Co-Founder and Managing Partner
We don't want an address listed
miles.t.grant@mailbox-demo.net
www.halcyonelitelasvegas-demo.com
We also need a second card with all of the same info except for the following changes: Name: Derek Malone Phone #: 555.014.7392 Email: Derek.Malonevip@mailbox-demo.net
Just use the logo

```html
<!DOCTYPE html>
<html lang="en">
<head>
<meta charset="utf-8">
<title>Halcyon Elite Las Vegas — Business Cards</title>
<link href="https://fonts.googleapis.com/css2?family=Montserrat:wght@400;600&display=swap" rel="stylesheet">
<style>
  :root {
    --bg: #e4e6e8;
    --card-black: #0b0b0d;
    --card-white: #ffffff;
    --blue: #2f8fe0;
    --blue-light: #6cc0f5;
    --blue-deep: #1461b8;
    --text-light: #e9eef3;
  }
  * { margin: 0; padding: 0; box-sizing: border-box; }
  html, body { width: 1200px; height: 1009px; overflow: hidden; }
  body {
    background: var(--bg);
    font-family: "Montserrat", Arial, sans-serif;
    position: relative;
  }
  .card {
    position: absolute;
    left: 220px;
    width: 760px;
    height: 434px;
    border-radius: 26px;
    overflow: hidden;
    box-shadow: 0 10px 30px rgba(0,0,0,.18);
  }
  .card-front { top: 58px; background: var(--card-black); }
  .card-back { top: 520px; background: var(--card-black); }

  .ornament-area {
    position: absolute;
    top: 0; right: 0; bottom: 0;
    width: 250px;
    background: linear-gradient(90deg, var(--blue-deep) 0%, var(--blue) 30%, var(--blue-light) 60%, var(--card-white) 100%);
  }

  .brand {
    position: absolute;
    color: var(--blue);
    font-weight: 600;
    letter-spacing: -0.5px;
    line-height: 1;
    white-space: nowrap;
  }
  .card-front .brand { left: 70px; top: 150px; font-size: 58px; }
  .brand-sub {
    position: absolute;
    color: var(--text-light);
    font-weight: 400;
    text-transform: uppercase;
    white-space: nowrap;
  }
  .card-front .brand-sub { left: 74px; top: 214px; font-size: 14px; letter-spacing: 6px; }
  .website-front {
    position: absolute;
    left: 74px; top: 246px;
    color: var(--text-light);
    font-size: 15px;
    letter-spacing: .5px;
    white-space: nowrap;
  }

  .back-band {
    position: absolute; left: 0; top: 0; bottom: 0; width: 24px;
    background: linear-gradient(180deg, var(--blue-light), var(--blue-deep));
  }
  .card-back .brand { left: 62px; top: 48px; font-size: 54px; }
  .card-back .brand-sub { left: 66px; top: 110px; font-size: 15px; letter-spacing: 8px; }
  .tagline {
    position: absolute; left: 66px; top: 134px;
    color: var(--blue);
    font-size: 11px; letter-spacing: 2px; text-transform: uppercase;
    white-space: nowrap;
  }
  .contact-list {
    position: absolute; left: 66px; top: 214px;
    list-style: none;
    color: var(--text-light);
    font-size: 16px;
  }
  .contact-list li { display: flex; align-items: center; gap: 12px; height: 34px; white-space: nowrap; }
  .contact-list svg { width: 16px; height: 16px; fill: var(--text-light); flex: none; }
  .person {
    position: absolute; right: 56px; top: 300px; text-align: right;
  }
  .person-name { color: var(--blue); font-size: 22px; font-weight: 600; }
  .person-title { color: var(--text-light); font-size: 15px; margin-top: 8px; white-space: nowrap; }
</style>
</head>
<body>

<section class="card card-front">
  <div class="ornament-area" role="img" aria-label="Decorative blue swoosh ornament sweeping down the right side of the card"></div>
  <div class="brand">Halcyon Elite</div>
  <div class="brand-sub">Las Vegas</div>
  <div class="website-front">www.halcyonelitelasvegas-demo.com</div>
</section>

<section class="card card-back">
  <div class="back-band"></div>
  <div class="brand">Halcyon Elite</div>
  <div class="brand-sub">Las Vegas</div>
  <div class="tagline">VIP Concierge &amp; Casino Hosting</div>

  <ul class="contact-list">
    <li>
      <svg viewBox="0 0 16 16"><rect x="1" y="1" width="14" height="14" rx="2"/></svg>
      VIP Line
    </li>
    <li>
      <svg viewBox="0 0 16 16"><path d="M3 1h3l1.5 4-2 1.5a9 9 0 0 0 4 4L11 8.5l4 1.5v3a2 2 0 0 1-2 2A12 12 0 0 1 1 3a2 2 0 0 1 2-2z"/></svg>
      555.014.7392
    </li>
    <li>
      <svg viewBox="0 0 16 16"><path d="M1 3h14v10H1z M1 3l7 6 7-6" fill="none" stroke="#e9eef3" stroke-width="1.6"/></svg>
      miles.t.grant@mailbox-demo.net
    </li>
    <li>
      <svg viewBox="0 0 16 16"><circle cx="8" cy="8" r="6.5" fill="none" stroke="#e9eef3" stroke-width="1.5"/><path d="M1.5 8h13M8 1.5c-3 3.5-3 9.5 0 13M8 1.5c3 3.5 3 9.5 0 13" fill="none" stroke="#e9eef3" stroke-width="1.2"/></svg>
      www.halcyonelitelasvegas-demo.com
    </li>
  </ul>

  <div class="person">
    <div class="person-name">Miles Grant</div>
    <div class="person-title">Co-Founder and Managing Partner</div>
  </div>
</section>

</body>
</html>
```